Banner Ad Design Project: Velvet Apron Parlor

VelvetApronParlor.com is a community/personals website for those who enjoy the Sissy Maid Fetish.

Our membership typically falls into 3 categories:
1) Dominant women, men and transgendered people,
2) Submissive women, men and transgender people, and
3) People who can be either dominant or submissive (switches).

The fetish itself can involve a dominant or dominants along with sissy maids.

VelvetApronParlor.com is not a porn website but it is meant for adult members.

What I need are 2 sizes of advertising banners:
1) 468 x 60 banner
2) 160 x 600 banner

You can checkout my website at: http://velvetapronparlor.example
Use the username: reviewer
and the password: reviewer

I've attached 4 files, but there's no requirement that you use any of them. Graphics done by yourselves is OK also.

Target Market(s)

The target market is men; Straight, Bi & Gay and women; Straight, Bi & Gay.

Industry/Entity Type

Advertising

Requirements
Must have
• It should have Join Now somewhere on the banner,
It should indicate that the website is; a community for those interested in the sissy maid fetish

```html
<!DOCTYPE html>
<html lang="en">
<head>
<meta charset="utf-8">
<title>Velvet Apron Parlor – Skyscraper Banner</title>
<link rel="stylesheet" href="https://fonts.googleapis.com/css2?family=Open+Sans:wght@400;600;800&display=swap">
<style>
  :root {
    --ink: #000000;
    --white: #ffffff;
    --stripe-top: #d32a30;
    --stripe-bottom: #a81c22;
    --magenta-light: #ff63de;
    --magenta: #f500c4;
    --magenta-deep: #e400b2;
    --button-rim: #f9b6ec;
    --button-shadow: #5a0048;
    --art-paper: #ffffff;
    --art-dress: #1c1f3a;
    --art-apron: #f4f2ee;
    --art-hair: #8a4a22;
    --art-skin: #f1c9a8;
  }
  html, body {
    margin: 0;
    padding: 0;
    width: 1200px;
    height: 4505px;
    overflow: hidden;
    background: var(--ink);
  }
  .banner {
    position: relative;
    width: 1200px;
    height: 4505px;
    background: var(--ink);
    font-family: "Open Sans", Arial, sans-serif;
    color: var(--white);
  }
  .headline-band {
    position: absolute;
    left: 0; top: 0;
    width: 1200px; height: 338px;
    display: flex;
    align-items: center;
    justify-content: center;
  }
  .headline-band h1 {
    margin: 0;
    font-weight: 400;
    font-size: 116px;
    letter-spacing: -1px;
    white-space: nowrap;
  }
  .accent-stripe {
    position: absolute;
    left: 0; top: 338px;
    width: 1200px; height: 40px;
    background: linear-gradient(var(--stripe-top), var(--stripe-bottom));
  }
  .pitch-panel {
    position: absolute;
    left: 0; top: 378px;
    width: 1200px; height: 1944px;
    background: linear-gradient(180deg, var(--magenta-light) 0%, var(--magenta) 45%, var(--magenta-deep) 100%);
    text-align: center;
  }
  .pitch-title {
    position: absolute;
    left: 0; top: 60px;
    width: 100%;
    margin: 0;
    font-weight: 600;
    font-size: 134px;
    line-height: 180px;
    letter-spacing: -1px;
    white-space: nowrap;
  }
  .pitch-copy {
    position: absolute;
    left: 0; top: 290px;
    width: 100%;
    margin: 0;
    font-weight: 400;
    font-size: 124px;
    line-height: 160px;
    letter-spacing: -1px;
    white-space: nowrap;
  }
  .pitch-arrow {
    position: absolute;
    left: 420px; top: 1145px;
    width: 360px; height: 490px;
    filter: drop-shadow(10px 14px 10px rgba(90, 0, 70, 0.55));
  }
  .site-address {
    position: absolute;
    left: 0; top: 1694px;
    width: 100%;
    margin: 0;
    font-size: 92px;
    line-height: 126px;
    letter-spacing: -2px;
    white-space: nowrap;
  }
  .mascot-art {
    position: absolute;
    left: 0; top: 2405px;
    width: 1200px; height: 1584px;
    background:
      radial-gradient(ellipse 230px 170px at 610px 170px, rgba(138, 74, 34, 0.55), rgba(138, 74, 34, 0) 100%),
      radial-gradient(ellipse 180px 140px at 620px 360px, rgba(241, 201, 168, 0.7), rgba(241, 201, 168, 0) 100%),
      radial-gradient(ellipse 260px 420px at 760px 1010px, rgba(244, 242, 238, 0.95), rgba(244, 242, 238, 0) 100%),
      radial-gradient(ellipse 380px 560px at 740px 960px, rgba(28, 31, 58, 0.55), rgba(28, 31, 58, 0) 100%),
      linear-gradient(180deg, var(--art-paper), #f3f3f7);
  }
  .cta-band {
    position: absolute;
    left: 0; top: 3989px;
    width: 1200px; height: 516px;
    display: flex;
    align-items: center;
    justify-content: center;
  }
  .join-button {
    width: 1020px;
    height: 244px;
    box-sizing: border-box;
    border: 10px solid var(--button-rim);
    border-radius: 122px;
    background: linear-gradient(180deg, var(--magenta-light) 0%, var(--magenta) 55%, var(--magenta-deep) 100%);
    display: flex;
    align-items: center;
    justify-content: center;
    font-family: "Open Sans", Arial, sans-serif;
    font-weight: 800;
    font-size: 158px;
    letter-spacing: -2px;
    color: var(--white);
    text-shadow: 8px 8px 6px var(--button-shadow);
    text-decoration: none;
    white-space: nowrap;
  }
</style>
</head>
<body>
  <div class="banner">
    <header class="headline-band">
      <h1>The Best Community</h1>
    </header>
    <div class="accent-stripe"></div>

    <section class="pitch-panel">
      <h2 class="pitch-title">Sissy Maid Fetish</h2>
      <p class="pitch-copy">for the pleasure of<br>Dommes, Masters,<br>sissies, maids and<br>sissy maids<br>everywhere.</p>
      <svg class="pitch-arrow" viewBox="0 0 360 490" aria-hidden="true">
        <polygon points="120,0 240,0 240,190 345,190 180,480 15,190 120,190" fill="#ffffff"/>
      </svg>
      <p class="site-address">www.VelvetApronParlor.com</p>
    </section>

    <div class="mascot-art" role="img" aria-label="Cartoon illustration of a brown-haired maid in a navy dress and white apron, waving a feather duster"></div>

    <footer class="cta-band">
      <a class="join-button" href="http://velvetapronparlor.example">JOIN NOW</a>
    </footer>
  </div>
</body>
</html>
```